Letterhead and Business card for Construction company

We need a letterhead and business card with our new company logo. We are based in NY. We develop and build properties.

The design should incorporate some unique feature from the logo (shape, font...). it should look like an extension from it.

Design should be clean and elegant, professional, not too busy.

The letterhead should include:
Logo (attached)
Address
Phone
Email

Please find the attached logo images and AI file.

Target Market(s)

Construction industry professionals

Industry/Entity Type

Construction, Development

Font styles to use
Sans Serif

Colors

Designer to choose colors to be used in the design.

Requirements
Must have
• Design should incorporate logo elements, additional assets are welcome. I'd like to see some other shapes / images invorporated too.

```html
<!DOCTYPE html>
<html lang="en">
<head>
<meta charset="utf-8">
<title>Norbrook Builders – Stationery</title>
<link href="https://fonts.googleapis.com/css2?family=Open+Sans:wght@400;600;700;800&family=Pinyon+Script&display=swap" rel="stylesheet">
<style>
  :root {
    --backdrop: #555555;
    --paper: #f2f2f2;
    --card-white: #ffffff;
    --ink: #231f20;
    --ink-soft: #3a3a3a;
    --orange: #ee7a1e;
    --dark: #231f20;
    --light-text: #ffffff;
    --ghost: #2e2c2c;
  }
  * { box-sizing: border-box; margin: 0; padding: 0; }
  html, body { width: 1200px; height: 1000px; overflow: hidden; }
  body {
    background: var(--backdrop);
    font-family: "Open Sans", Arial, sans-serif;
    color: var(--ink-soft);
    position: relative;
  }

  /* ---------- Letterhead ---------- */
  .letterhead {
    position: absolute; left: 40px; top: 45px;
    width: 640px; height: 905px;
    background: var(--paper);
    overflow: hidden;
  }
  .brand {
    display: flex; align-items: center; gap: 8px;
    font-weight: 800; color: var(--ink);
    letter-spacing: 0.5px; line-height: 1;
  }
  .brand-mark { width: 14px; height: 14px; background: var(--orange); flex: none; }
  .letterhead .brand { position: absolute; left: 56px; top: 62px; font-size: 25px; }
  .brand-text small { display: block; font-size: 0.52em; letter-spacing: 3px; margin-top: 4px; }
  .sender-address {
    position: absolute; right: 55px; top: 48px;
    text-align: right; font-size: 11px; line-height: 13px; color: var(--ink);
  }
  .letter-body {
    position: absolute; left: 87px; top: 220px; width: 467px;
    font-size: 10.4px; line-height: 15px; text-align: justify;
  }
  .letter-body p { margin-bottom: 15px; }
  .letter-body .salutation { margin-bottom: 15px; }
  .closing { position: absolute; left: 87px; top: 624px; font-size: 10.4px; }
  .signature {
    font-family: "Pinyon Script", cursive;
    font-size: 22px; color: var(--ink); margin-top: 4px;
  }
  .skyline-art {
    position: absolute; left: 370px; top: 655px; width: 270px; height: 215px;
    background: linear-gradient(180deg, rgba(210,210,210,0) 0%, #dcdcdc 45%, #d8d8d8 100%);
  }
  .letter-footer { position: absolute; left: 0; bottom: 0; width: 640px; height: 110px; }
  .footer-contacts {
    position: absolute; left: 55px; bottom: 24px;
    color: var(--light-text); font-size: 11px; line-height: 14px;
  }
  .contact-line { display: flex; align-items: center; gap: 4px; }
  .contact-line svg { flex: none; }

  /* ---------- Business cards ---------- */
  .card {
    position: absolute; left: 725px; width: 440px; height: 270px; overflow: hidden;
  }
  .card-front { top: 175px; background: var(--card-white); }
  .card-back { top: 520px; background: var(--dark); display: flex; align-items: center; justify-content: center; }
  .holder { position: absolute; left: 36px; top: 46px; }
  .holder-name { color: var(--orange); font-weight: 800; font-size: 14px; letter-spacing: 0.3px; }
  .holder-role { font-size: 10px; color: var(--ink); margin-top: -2px; }
  .card-front .brand { position: absolute; right: 40px; top: 52px; font-size: 21px; }
  .card-wave { position: absolute; left: 0; top: 90px; width: 440px; height: 180px; }
  .card-details {
    position: absolute; left: 36px; top: 168px;
    color: var(--light-text); font-size: 9.5px; line-height: 12px;
  }
  .card-details .contacts { margin-top: 8px; }
  .card-web { position: absolute; right: 40px; bottom: 24px; color: var(--light-text); font-size: 9.5px; }
  .card-back .brand { color: var(--ghost); font-size: 34px; }
  .card-back .brand-mark { background: var(--ghost); width: 18px; height: 18px; }
</style>
</head>
<body>

<section class="letterhead" aria-label="Letterhead">
  <div class="brand">
    <span class="brand-mark"></span>
    <span class="brand-text">NORBROOK<small>BUILDERS</small></span>
  </div>
  <address class="sender-address" style="font-style:normal">
    PO Box 4000<br>Co. Street, Building/Suite<br>City/State, Zip Code
  </address>

  <div class="letter-body">
    <p class="salutation">Dear Martin Cole,</p>
    <p>Lorem ipsum dolor sit amet, consectetuer adipiscing elit, sed diam nonummy nibh euismod tincidunt ut laoreet dolore magna aliquam erat volutpat. Ut wisi enim ad minim veniam, quis nostrud exerci tation ullamcorper suscipit lobortis nisl ut aliquip ex ea commodo consequat. Duis dolore te feugait nulla facilisi. Nam liber tempor cum soluta nobis eleifend option congue nihil imperdiet doming id quod mazim placerat facer possim assum. Lorem ipsum dolor sit amet, consectetuer adipiscing elit, sed diam nonummy nibh euismod tincidunt ut laoreet dolore magna aliquam erat volutpat. Ut wisi enim ad minim veniam, quis nostrud exerci tation ullamcorper suscipit lobortis nisl ut aliquip ex ea commodo consequat.</p>
    <p>Consectetuer adipiscing elit, sed diam nonummy nibh euismod tincidunt ut laoreet dolore magna aliquam erat volutpat. Ut wisi enim ad minim veniam, quis nostrud exerci tation ullamcorper suscipit lobortis nisl ut aliquip ex ea commodo consequat. Consectetuer adipiscing elit, sed diam nonummy nibh euismod tincidunt ut laoreet dolore magna aliquam erat volutpat. Ut wisi enim ad minim veniam, quis nostrud exerci tation ullamcorper suscipit lobortis nisl ut aliquip ex ea commodo consequat.</p>
    <p>Consectetuer adipiscing elit, sed diam nonummy nibh euismod tincidunt ut laoreet dolore magna aliquam erat volutpat. Ut wisi enim ad minim veniam, quis nostrud exerci tation ullamcorper suscipit lobortis nisl ut aliquip ex ea commodo consequat. Consectetuer adipiscing elit, sed diam nonummy nibh euismod tincidunt ut laoreet dolore magna aliquam erat volutpat. Ut wisi enim ad minim veniam, quis nostrud exerci tation ullamcorper suscipit lobortis nisl ut aliquip ex ea commodo consequat.</p>
  </div>

  <div class="closing">
    <p>Sincerely Yours</p>
    <p class="signature">Thomas Reed</p>
  </div>

  <div class="skyline-art" role="img" aria-label="Faint grey city skyline of tall buildings"></div>

  <svg class="letter-footer" viewBox="0 0 640 110" preserveAspectRatio="none" aria-hidden="true">
    <path fill="var(--orange)" d="M0,5 C180,-5 320,40 430,70 C520,92 590,80 640,60 L640,76 C590,95 520,104 430,86 C320,58 180,20 0,28 Z"/>
    <path fill="var(--dark)" d="M0,38 C180,30 320,68 430,95 C520,112 590,100 640,88 L640,110 L0,110 Z"/>
    <path fill="none" stroke="var(--orange)" stroke-width="2" d="M250,58 C340,72 400,96 470,100 C540,104 590,96 630,86"/>
  </svg>
  <div class="footer-contacts">
    <div class="contact-line">
      <svg width="9" height="9" viewBox="0 0 10 10"><path fill="var(--orange)" d="M2,0 L4,2.5 L3,3.8 C3.8,5.4 4.6,6.2 6.2,7 L7.5,6 L10,8 L8.5,10 C4,9.5 0.5,6 0,1.5 Z"/></svg>
      <span>0400 555 0123</span>
    </div>
    <div class="contact-line">
      <svg width="9" height="9" viewBox="0 0 10 10"><rect x="0" y="2" width="10" height="7" fill="var(--orange)"/><path d="M0,2 L5,6 L10,2" fill="none" stroke="var(--dark)" stroke-width="1"/></svg>
      <span>info@norbrookbuilders.com</span>
    </div>
  </div>
</section>

<section class="card card-front" aria-label="Business card front">
  <div class="holder">
    <p class="holder-name">DANIEL HARTLEY</p>
    <p class="holder-role">Founder &amp; CEO</p>
  </div>
  <div class="brand">
    <span class="brand-mark"></span>
    <span class="brand-text">NORBROOK<small>BUILDERS</small></span>
  </div>
  <svg class="card-wave" viewBox="0 0 440 180" preserveAspectRatio="none" aria-hidden="true">
    <path fill="var(--orange)" d="M0,3 C100,-8 170,25 230,55 C300,90 380,95 440,62 L440,74 C380,108 300,104 230,70 C170,40 100,12 0,22 Z"/>
    <path fill="var(--dark)" d="M0,30 C100,20 170,50 230,80 C300,112 380,116 440,86 L440,180 L0,180 Z"/>
    <path fill="none" stroke="var(--orange)" stroke-width="1.6" d="M180,70 C240,100 300,118 360,112"/>
  </svg>
  <div class="card-details">
    <p>PO Box 4000<br>Co. Street, Building/Suite<br>City/State, Zip Code</p>
    <div class="contacts">
      <div class="contact-line">
        <svg width="8" height="8" viewBox="0 0 10 10"><path fill="var(--orange)" d="M2,0 L4,2.5 L3,3.8 C3.8,5.4 4.6,6.2 6.2,7 L7.5,6 L10,8 L8.5,10 C4,9.5 0.5,6 0,1.5 Z"/></svg>
        <span>0400 555 0123</span>
      </div>
      <div class="contact-line">
        <svg width="8" height="8" viewBox="0 0 10 10"><rect x="0" y="2" width="10" height="7" fill="var(--orange)"/><path d="M0,2 L5,6 L10,2" fill="none" stroke="var(--dark)" stroke-width="1"/></svg>
        <span>info@norbrookbuilders.com</span>
      </div>
    </div>
  </div>
  <p class="card-web">www.norbrookbuilders.com</p>
</section>

<section class="card card-back" aria-label="Business card back">
  <div class="brand">
    <span class="brand-mark"></span>
    <span class="brand-text">NORBROOK<small>BUILDERS</small></span>
  </div>
</section>

</body>
</html>
```